Brightway Dwelling & Yard Care - Maintenance & Improvements

Handyman service - Total home improvement and maintenance

We do everything indoors, ie. carpentry, and outdoors, ie. garden maintenance

No job too small or too unusual

7 Days per week
Updates

I want the overall impression not to favour either gender ... eg. maybe don't use the word Handy'man' because we also have a Fixmistress service .... but just stay with a generic theme of home improvement and maintenance

Industry/Entity Type

Home Improvement

Contact Information for Business Card

Brightway Dwelling & Yard Care
7 Days per Week
Total Home Maintenance and Improvements
Handyman | Fixmistress | Our (DIY) Task Pal
Ph: 0487 613 902
www.brightwaydwellingyard.com.au

Requirements
Must have
• The black and white image of various workers, as per attached

```html
<!DOCTYPE html>
<html lang="en">
<head>
<meta charset="utf-8">
<title>Brightway Dwelling &amp; Yard Care – Business Card</title>
<link href="https://fonts.googleapis.com/css2?family=Playfair+Display:wght@700&family=Cormorant+SC:wght@500&family=Open+Sans:wght@400;600&display=swap" rel="stylesheet">
<style>
  :root {
    --bg: #e9e6df;
    --green-light: #a6d651;
    --green-mid: #8cc43a;
    --green-dark: #6fa823;
    --ink: #1c1c1c;
    --rule: #111111;
    --paper: #ffffff;
    --paper-shade: #eeeeee;
    --photo-dark: #3f5a2c;
    --photo-light: #8fa874;
    --accent: #9ccc4a;
    --figure-light: #8a8a8a;
    --figure-dark: #2a2a2a;
  }
  * { box-sizing: border-box; margin: 0; padding: 0; }
  html, body { width: 1200px; height: 1023px; overflow: hidden; background: var(--bg); }
  .stage { width: 1200px; height: 1023px; display: flex; align-items: center; justify-content: center; }
  .card {
    position: relative; width: 900px; height: 514px; border-radius: 22px; overflow: hidden;
    background: var(--paper); box-shadow: 0 6px 24px rgba(0,0,0,.18);
  }
  .brand-band {
    position: absolute; left: 0; top: 0; width: 540px; height: 200px;
    background: linear-gradient(180deg, var(--green-light), var(--green-mid) 60%, var(--green-dark));
    border-bottom: 6px solid var(--rule);
    padding: 34px 0 0 40px;
  }
  .brand-name {
    font-family: "Playfair Display", serif; font-weight: 700; font-size: 36px;
    line-height: 1.05; color: var(--ink); letter-spacing: .5px;
  }
  .tagline {
    margin-top: 18px; font-family: "Open Sans", sans-serif; font-size: 15px;
    line-height: 1.55; color: var(--ink);
  }
  .garden-photo {
    position: absolute; left: 546px; top: 0; width: 354px; height: 380px;
    background: linear-gradient(160deg, var(--photo-light), var(--photo-dark));
    border-left: 6px solid var(--rule);
  }
  .contact-panel {
    position: absolute; left: 0; top: 206px; width: 540px; height: 174px;
    background: linear-gradient(180deg, var(--paper), var(--paper-shade));
    padding: 26px 0 0 40px;
  }
  .task-pal {
    font-family: "Cormorant SC", serif; font-weight: 500; font-size: 34px;
    color: var(--accent); letter-spacing: 1px;
  }
  .contact-line {
    display: flex; align-items: center; gap: 12px; margin-top: 12px;
    font-family: "Open Sans", sans-serif; font-size: 16px; color: var(--ink);
  }
  .contact-line svg { flex: none; }
  .worker-strip {
    position: absolute; left: 0; top: 380px; width: 900px; height: 134px;
    border-top: 6px solid var(--rule);
    background: linear-gradient(180deg, var(--paper), var(--paper-shade));
    display: flex; align-items: center; justify-content: space-between;
    padding: 0 34px;
  }
  .worker-figure {
    width: 62px; height: 86px; border-radius: 10px;
    background: radial-gradient(ellipse at 50% 40%, var(--figure-dark), var(--figure-light) 75%, transparent 100%);
    opacity: .85;
  }
</style>
</head>
<body>
<main class="stage">
  <article class="card">
    <header class="brand-band">
      <h1 class="brand-name">Brightway Dwelling<br>&amp; Yard Care</h1>
      <p class="tagline">7 Days per Week Total Home | Maintenance and Improvements<br>Handyman | Fixmistress | Our (DIY)</p>
    </header>
    <div class="garden-photo" role="img" aria-label="Photograph of a leafy garden with a wooden window frame"></div>
    <section class="contact-panel">
      <p class="task-pal">Task Pal</p>
      <p class="contact-line">
        <svg width="16" height="16" viewBox="0 0 16 16" aria-hidden="true"><rect width="16" height="16" rx="2" fill="#9ccc4a"/><rect x="5" y="3" width="6" height="10" rx="1" fill="#fff"/></svg>
        0487 613 902
      </p>
      <p class="contact-line">
        <svg width="16" height="16" viewBox="0 0 16 16" aria-hidden="true"><rect width="16" height="16" rx="2" fill="#9ccc4a"/><circle cx="8" cy="8" r="4.5" fill="none" stroke="#fff" stroke-width="1.5"/></svg>
        www.brightwaydwellingyard.com.au
      </p>
    </section>
    <div class="worker-strip">
      <div class="worker-figure" role="img" aria-label="Black pictogram of a worker sawing timber"></div>
      <div class="worker-figure" role="img" aria-label="Black pictogram of a worker fixing a sink"></div>
      <div class="worker-figure" role="img" aria-label="Black pictogram of a worker painting a wall"></div>
      <div class="worker-figure" role="img" aria-label="Black pictogram of a worker on a ladder"></div>
      <div class="worker-figure" role="img" aria-label="Black pictogram of a worker drilling"></div>
      <div class="worker-figure" role="img" aria-label="Black pictogram of a worker trimming a hedge"></div>
      <div class="worker-figure" role="img" aria-label="Black pictogram of a worker mowing a lawn"></div>
      <div class="worker-figure" role="img" aria-label="Black pictogram of a worker planting"></div>
      <div class="worker-figure" role="img" aria-label="Black pictogram of a worker spreading seed"></div>
      <div class="worker-figure" role="img" aria-label="Black pictogram of a worker watering with a hose"></div>
    </div>
  </article>
</main>
</body>
</html>
```